Hummingfern Bramble Dabs - our own unique product line of cotton swabs

We have something now that we are not too happy with. Looking to create a label for a line of cotton swabs that we have created and designed to clean your nose from mucus and boogers. The logo that i have so far for the packaging is the white background with the black silhouette nose (attached). We need something that can do well in the retail/consumer market. Our website address (even though it is not live yet) should be listed somewhere on the label....
www.HummingfernBramble.example ( we sell pillows, but we have other product lines)
We would also like to see a brief description on how to correctly use the nose pick on the back side of the label. The description on how to use should read " insert cotton nose pick into nostril and give it a few counter clock wise twirls or till you feel mucus/debris latch onto the cotton. You may need to repeat the process and use more than one nose pick to achieve desired result."
As well as a warning mentioning : "Never insert plastic end of nose pick into any part of your body. Be careful and use with caution."
Also for you to know, the cotton is made from 100% natural cotton, the cotton head itself is thick and highly absorbent making it a pleasure to use. There are 50 nose picks per pack.
We're fine with keeping it simple and not making the packaging too busy, however we're open to your ideas and designs! I have given you the most important information relevant to the project. If there are any questions or something is not clear enough please kindly message me.

Requirements
Must have
• professional looking
clean looking
not busy
Should not have
• words clumping together making it appear as too much text in one area
too much text clumped together on the design

```html
<!DOCTYPE html>
<html lang="en">
<head>
<meta charset="utf-8">
<title>Hummingfern Bramble Dabs – Cotton Swabs Label</title>
<link rel="stylesheet" href="https://fonts.googleapis.com/css2?family=Ubuntu:wght@400&family=Rubik:ital,wght@1,700;1,900&display=swap">
<style>
  :root {
    --backdrop: #e6e7e9;
    --label-white: #ffffff;
    --ink: #141414;
    --orange: #f05a28;
    --navy: #0a2c47;
    --teal: #128a8a;
  }
  * { box-sizing: border-box; margin: 0; padding: 0; }
  html, body {
    width: 1200px;
    height: 708px;
    overflow: hidden;
    background: var(--backdrop);
  }
  .canvas {
    position: relative;
    width: 1200px;
    height: 708px;
  }
  .label {
    position: absolute;
    left: 252px;
    top: 54px;
    width: 698px;
    height: 600px;
    background: var(--label-white);
    overflow: hidden;
    box-shadow: 3px 4px 8px rgba(0, 0, 0, 0.25);
  }
  .label__artwork {
    position: absolute;
    inset: 0;
    background: linear-gradient(150deg,
      rgba(255, 255, 255, 0) 48%,
      rgba(18, 138, 138, 0.55) 66%,
      var(--teal) 76%,
      var(--navy) 96%);
  }
  .brand {
    position: absolute;
    left: 110px;
    top: 58px;
    width: 480px;
    text-align: center;
    font-family: "Ubuntu", sans-serif;
    font-weight: 400;
    color: var(--ink);
    line-height: 1;
  }
  .brand__name {
    display: block;
    font-size: 52px;
    letter-spacing: -0.5px;
  }
  .brand__sub {
    display: block;
    margin-top: 8px;
    font-size: 32px;
  }
  .brand__line {
    display: block;
    margin-top: 16px;
    font-size: 20px;
    letter-spacing: 6px;
  }
  .product-title {
    position: absolute;
    left: 48px;
    top: 274px;
    font-family: "Rubik", sans-serif;
    font-style: italic;
    font-weight: 900;
    color: var(--orange);
    line-height: 1.08;
    text-transform: uppercase;
  }
  .product-title__top { display: block; font-size: 62px; }
  .product-title__bottom { display: block; font-size: 74px; }
  .web-pill {
    position: absolute;
    left: 116px;
    top: 521px;
    width: 464px;
    height: 40px;
    border-radius: 20px;
    background: var(--orange);
    color: var(--label-white);
    font-family: "Rubik", sans-serif;
    font-style: italic;
    font-weight: 700;
    font-size: 19px;
    display: flex;
    align-items: center;
    justify-content: center;
  }
</style>
</head>
<body>
<main class="canvas">
  <section class="label">
    <div class="label__artwork" role="img" aria-label="Decorative sweep of teal, navy and gold bands rising to the lower right"></div>

    <div class="brand">
      <span class="brand__name">Hummingfern</span>
      <span class="brand__sub">Bramble</span>
      <span class="brand__line">Dabs</span>
    </div>

    <h1 class="product-title">
      <span class="product-title__top">Cotton</span>
      <span class="product-title__bottom">Swabs</span>
    </h1>

    <div class="web-pill">www.HummingfernBramble.example</div>
  </section>
</main>
</body>
</html>
```